rk ironcraft business card metallic look

revamp the existing design but want card to have a metalic look to it

Target Market(s)

construction industry

Industry/Entity Type

constrction

Contact Information for Business Card

front of card RK Ironcraft, phone 4165550193, email rk.ironcraftt@veltrano.com and instagram account; rk_ironcraft_

Font styles to use
Other font styles liked:
• masculine

Colors

Designer to choose only greyscale colors for use in the design.

Requirements
Must have
• back side RK Ironcraft then a list of everything : Siding, ACM Panels, Standing Seam,Soffit, Fascia, Gutters,Metal,Alu,inum, Viynyl, Metal Roofs and roof repairs
Nice to have
• I would like to keep the look of the existing card with the metal grids on the front
Should not have
• Need a design in two days

```html
<!DOCTYPE html>
<html lang="en">
<head>
<meta charset="UTF-8">
<title>RK Ironcraft — Business Card</title>
<link href="https://fonts.googleapis.com/css2?family=Oswald:wght@500;700&family=Josefin+Sans:wght@400&display=swap" rel="stylesheet">
<style>
  :root{
    --page:#2b2b2d;
    --card-dark:#0a0a0b;
    --card-mid:#1c1c1e;
    --steel-hi:#4a4a4d;
    --steel-edge:rgba(200,200,205,.22);
    --steel:#b8b4ab;
    --steel-soft:#9a968f;
    --ghost:#242426;
    --ink-light:#d8d8d8;
  }
  *{margin:0;padding:0;box-sizing:border-box}
  html,body{width:1200px;height:942px;overflow:hidden;background:var(--page)}
  .sheet{
    width:1200px;height:942px;
    display:flex;align-items:center;justify-content:center;gap:40px;
  }
  .card{
    position:relative;width:540px;height:309px;border-radius:22px;overflow:hidden;
    background:var(--card-dark);
    border:1px solid var(--steel-edge);
    box-shadow:0 18px 40px rgba(0,0,0,.55), inset 0 1px 0 rgba(255,255,255,.12);
  }
  .card__texture{
    position:absolute;inset:0;
    background:
      linear-gradient(115deg, rgba(255,255,255,0) 30%, rgba(255,255,255,.07) 42%, rgba(255,255,255,.02) 48%, rgba(255,255,255,0) 56%),
      repeating-linear-gradient(90deg, rgba(255,255,255,.025) 0 1px, rgba(0,0,0,0) 1px 3px),
      radial-gradient(ellipse at 58% 18%, var(--steel-hi) 0%, var(--card-mid) 42%, var(--card-dark) 85%);
  }
  .card--contact .card__texture{
    background:
      linear-gradient(120deg, rgba(255,255,255,0) 25%, rgba(255,255,255,.08) 45%, rgba(255,255,255,0) 62%),
      repeating-linear-gradient(90deg, rgba(255,255,255,.025) 0 1px, rgba(0,0,0,0) 1px 3px),
      radial-gradient(ellipse at 52% 14%, #56565a 0%, var(--card-mid) 40%, var(--card-dark) 82%);
  }
  .services__name{
    position:absolute;left:0;right:0;top:64px;text-align:center;
    font-family:"Oswald",sans-serif;font-weight:700;
    color:var(--steel);font-size:58px;letter-spacing:4px;text-transform:uppercase;line-height:1;
  }
  .services__list{
    position:absolute;left:20px;right:20px;top:180px;text-align:center;white-space:nowrap;
    font-family:"Oswald",sans-serif;font-weight:500;
    color:var(--steel-soft);font-size:12px;letter-spacing:1px;line-height:1.8;text-transform:uppercase;
  }
  .contact__ghost{
    position:absolute;left:0;right:0;top:72px;text-align:center;
    font-family:"Oswald",sans-serif;font-weight:700;
    color:var(--ghost);font-size:60px;letter-spacing:4px;text-transform:uppercase;line-height:1;
  }
  .contact__row{
    position:absolute;left:34px;right:30px;bottom:38px;
    display:flex;justify-content:space-between;align-items:flex-end;
    font-family:"Josefin Sans",sans-serif;color:var(--ink-light);font-size:14px;letter-spacing:1px;
  }
  .contact__item{display:flex;flex-direction:column;align-items:center;gap:8px}
  .contact__item svg{display:block}
  .contact__dot{width:11px;height:11px;border:1.4px solid var(--ink-light);border-radius:50%}
</style>
</head>
<body>
<main class="sheet">
  <section class="card card--services" aria-label="Card side with services">
    <div class="card__texture" role="img" aria-label="Dark brushed metal grid texture with steel sheen"></div>
    <h1 class="services__name">RK Ironcraft</h1>
    <p class="services__list">Sliding, ACM Panels, Standing Seam, Soffit, Fascia,<br>Gutters, Metal, Alu,inum, Viynyl, Metal Roofs and Roof Repairs</p>
  </section>

  <section class="card card--contact" aria-label="Card side with contact details">
    <div class="card__texture" role="img" aria-label="Dark brushed metal grid texture with soft steel highlight"></div>
    <p class="contact__ghost" aria-hidden="true">RK Ironcraft</p>
    <div class="contact__row">
      <div class="contact__item">
        <svg width="12" height="12" viewBox="0 0 24 24" aria-hidden="true"><path fill="#d8d8d8" d="M6.6 10.8c1.4 2.8 3.8 5.1 6.6 6.6l2.2-2.2c.3-.3.7-.4 1-.2 1.1.4 2.3.6 3.6.6.6 0 1 .4 1 1V20c0 .6-.4 1-1 1C10.6 21 3 13.4 3 4c0-.6.4-1 1-1h3.5c.6 0 1 .4 1 1 0 1.3.2 2.5.6 3.6.1.3 0 .7-.2 1z"/></svg>
        <span>416 - 555 - 0193</span>
      </div>
      <div class="contact__item">
        <svg width="13" height="10" viewBox="0 0 26 20" aria-hidden="true"><rect x="1" y="1" width="24" height="18" fill="none" stroke="#d8d8d8" stroke-width="2"/><path d="M1 1l12 10L25 1" fill="none" stroke="#d8d8d8" stroke-width="2"/></svg>
        <span>rk.ironcraftt@veltrano.com</span>
      </div>
      <div class="contact__item">
        <span class="contact__dot" aria-hidden="true"></span>
        <span>rk_ironcraft_</span>
      </div>
    </div>
  </section>
</main>
</body>
</html>
```